New Law Firm needs a business card design

I need a business card for my new law firm called Fenwick Estates and Trusts. I would like designs to use my logo attached. My firm is new and modern. I like the colors orange, white, grey and black. The design I will chose will be one which uses color well, one which looks impressive, smart and modern.

Target Market(s)

Adults aged 30 to 50 seeking professional advice.

Industry/Entity Type

Law Firm

Requirements
Must have
• My logo which is attached.

Must have a modern font, similar to my logo and draft business card.
Should not have
• Any symbols about law, such as scales etc.

```html
<!DOCTYPE html>
<html lang="en">
<head>
<meta charset="utf-8">
<title>Fenwick Estates and Trusts – Business Card</title>
<link rel="stylesheet" href="https://fonts.googleapis.com/css2?family=Source+Sans+3:wght@400;600;700&display=swap">
<style>
  :root {
    --orange: #f7901e;
    --black: #141414;
    --white: #ffffff;
    --grey: #8a8a8a;
    --grey-light: #cfcfcf;
    --ink: #222222;
    --backdrop: #d9d9db;
  }
  * { box-sizing: border-box; margin: 0; padding: 0; }
  html, body {
    width: 1200px; height: 900px; overflow: hidden;
    background: var(--backdrop);
    font-family: "Source Sans 3", Arial, sans-serif;
  }
  .sheet {
    position: relative; width: 1200px; height: 900px;
    display: flex; flex-direction: column; align-items: center; justify-content: center; gap: 40px;
  }
  .card {
    position: relative; width: 620px; height: 376px;
    background: var(--black); overflow: hidden;
    box-shadow: 0 6px 18px rgba(0,0,0,.18);
  }
  .card-art { position: absolute; inset: 0; }

  .wordmark {
    position: absolute; text-align: center;
    color: var(--grey); font-weight: 400; letter-spacing: .18em; text-transform: uppercase; line-height: 1.15;
  }
  .wordmark .mark-dot {
    display: inline-block; width: 10px; height: 10px; border-radius: 50%;
    background: var(--grey); margin-bottom: 6px;
  }

  /* front */
  .front .wordmark { left: 60px; top: 150px; width: 270px; font-size: 22px; }
  .service-list {
    position: absolute; left: 400px; top: 70px; list-style: none;
    color: var(--white); font-size: 19px; line-height: 1.28;
  }
  .service-list li::before { content: "•"; color: var(--orange); margin-right: 6px; }
  .liability-tag {
    position: absolute; left: 346px; top: 268px; width: 274px; height: 44px;
    background: var(--orange); border-radius: 8px 0 0 8px;
    color: var(--white); font-size: 12.5px; line-height: 1.2; padding: 5px 10px 0 14px;
  }

  /* back */
  .back .wordmark { left: 100px; top: 42px; width: 260px; font-size: 15px; }
  .contact {
    position: absolute; left: 90px; top: 100px; width: 280px; text-align: center;
    color: var(--ink); font-size: 14px; line-height: 1.25;
  }
  .contact .person-name { color: var(--orange); font-size: 27px; font-weight: 700; line-height: 1.05; }
  .contact .role { font-size: 14px; margin-bottom: 4px; }
  .contact .quals { font-size: 12.5px; margin-bottom: 6px; }
  .contact .address { margin-bottom: 8px; }
  .contact .label { color: var(--orange); }
  .web-band {
    position: absolute; left: 0; top: 302px; width: 620px; height: 36px;
    background: var(--orange); color: var(--white);
    font-size: 20px; font-weight: 600; padding-left: 120px; line-height: 36px;
  }
</style>
</head>
<body>
<main class="sheet">

  <section class="card front" aria-label="Card front">
    <svg class="card-art" viewBox="0 0 620 376" aria-hidden="true">
      <rect x="0" y="0" width="620" height="376" fill="var(--black)"/>
      <circle cx="190" cy="188" r="212" fill="none" stroke="var(--orange)" stroke-width="6"/>
      <circle cx="190" cy="188" r="200" fill="none" stroke="var(--grey)" stroke-width="10"/>
      <circle cx="190" cy="188" r="188" fill="none" stroke="var(--grey-light)" stroke-width="8"/>
      <circle cx="190" cy="188" r="180" fill="var(--white)"/>
    </svg>
    <div class="wordmark"><span class="mark-dot"></span><br>Fenwick<br>Estates &amp; Trusts</div>
    <ul class="service-list">
      <li>Wills</li>
      <li>Powers of Attorney</li>
      <li>Deceased Estate</li>
      <li>Will Disputes</li>
    </ul>
    <div class="liability-tag">Liability Limited by a scheme approved under professional standards legislation</div>
  </section>

  <section class="card back" aria-label="Card back">
    <svg class="card-art" viewBox="0 0 620 376" aria-hidden="true">
      <rect x="0" y="0" width="620" height="376" fill="var(--black)"/>
      <rect x="0" y="150" width="620" height="18" fill="var(--orange)"/>
      <circle cx="230" cy="190" r="196" fill="none" stroke="var(--orange)" stroke-width="5"/>
      <circle cx="230" cy="190" r="186" fill="none" stroke="var(--grey)" stroke-width="10"/>
      <circle cx="230" cy="190" r="175" fill="none" stroke="var(--grey-light)" stroke-width="8"/>
      <circle cx="230" cy="190" r="168" fill="var(--white)"/>
    </svg>
    <div class="wordmark">Fenwick<br>Estates &amp; Trusts</div>
    <div class="contact">
      <p class="person-name">Daniel Marsh</p>
      <p class="role">Lawyer</p>
      <p class="quals">Assoc.Deg.Law, BLJSt, LLB, Grad Dip Law.</p>
      <p class="address">Address: To be confirmed.</p>
      <p><span class="label">Phone:</span> To be confirmed</p>
      <p><span class="label">Fax:</span> To be confirmed</p>
      <p><span class="label">Email:</span> daniel@fenwicktrusts.com.au</p>
    </div>
    <div class="web-band">www.fenwicktrusts.com.au</div>
  </section>

</main>
</body>
</html>
```